inspirational business card

I want to use the Vector on Pixavend.com (number 58172046) and I will purchase the vector to send it to the designer once the general concept is approved. You can download it for free for a one time use on providing a design for this request.
Within the vector, insert:
Tessa Brundle
Guidance and Partnering

I prefer a vertical card but do not require vertical.

Contact info:

Tessa Brundle, J.D.
Collaborative Lawyer
Certified Divorce Coach
Mediation Coach
PHONE 515/555-0143
EMAIL: tbjd@quellmail.net

Website: Guidanceandpartnering.com
Settlementcourse.com

I like greens, blue and grey. I do not want black font, and would like the font to be legible without needing perfect reading vision (no super small font).
I would like the overall theme to convey growth and nurturance.
I like the vector I selected because of the growth and light portrayed.
Not too frilly or too bold. I would like to to appeal to both sexes.

Target Market(s)

Generally professional women 35-60

Industry/Entity Type

Attorney

Font styles to use
Serif
Sans Serif

Colors
acd136
cadf82
fbf289
9d9d9d

Requirements
Must have
• My project does not need to have my photo but you could use it if you want
Nice to have
• Vertical
• I like rounded edges on the cards
Should not have
• I do not like my name appearing two times in close proximity. I'm not a flowery person.

```html
<!DOCTYPE html>
<html lang="en">
<head>
<meta charset="utf-8">
<title>Tessa Brundle — Business Card</title>
<link href="https://fonts.googleapis.com/css2?family=Cormorant+Garamond:wght@500;600&family=Lato:wght@300;400&display=swap" rel="stylesheet">
<style>
  :root {
    --page-bg: #e9e6e1;
    --card-green: #acd136;
    --card-green-deep: #97bf22;
    --card-green-light: #cadf82;
    --card-text: rgba(255, 255, 255, 0.82);
    --card-text-soft: rgba(255, 255, 255, 0.72);
    --seal-bg: rgba(240, 239, 233, 0.88);
    --seal-text: #6f6f6b;
    --seal-dot: #9dc22a;
  }
  * { margin: 0; padding: 0; box-sizing: border-box; }
  html, body {
    width: 1200px;
    height: 1047px;
    overflow: hidden;
    background: var(--page-bg);
  }
  .business-card {
    position: absolute;
    left: 100px;
    top: 252px;
    width: 1000px;
    height: 543px;
    border-radius: 26px;
    background:
      radial-gradient(ellipse at 22% 55%, var(--card-green-light) 0%, rgba(202,223,130,0) 55%),
      linear-gradient(100deg, var(--card-green) 0%, var(--card-green-deep) 100%);
    box-shadow: 0 10px 30px rgba(60, 70, 30, 0.18);
    overflow: hidden;
  }
  .serif { font-family: "Cormorant Garamond", "Times New Roman", serif; }
  .sans { font-family: "Lato", Arial, sans-serif; }

  .brand-line {
    position: absolute;
    left: 43px;
    top: 52px;
    color: var(--card-text);
  }
  .brand-line .brand-name {
    font-size: 40px;
    font-weight: 500;
    letter-spacing: 1px;
    line-height: 1;
    text-transform: uppercase;
  }
  .brand-line .brand-tag {
    margin-top: 6px;
    padding-left: 56px;
    font-size: 13px;
    letter-spacing: 1.2px;
    text-transform: uppercase;
  }

  .person {
    position: absolute;
    left: 43px;
    top: 238px;
    color: var(--card-text);
  }
  .person .person-name {
    font-size: 28px;
    font-weight: 500;
    letter-spacing: 1.2px;
    text-transform: uppercase;
    line-height: 1;
  }
  .person .person-role {
    font-size: 20px;
    font-weight: 300;
    line-height: 27px;
    color: var(--card-text-soft);
  }
  .person .person-role:first-of-type { margin-top: 10px; }

  .contact-list {
    position: absolute;
    left: 43px;
    top: 394px;
    list-style: none;
    color: var(--card-text-soft);
    font-size: 21px;
    font-weight: 300;
    letter-spacing: 0.6px;
  }
  .contact-list li {
    display: flex;
    align-items: center;
    height: 31px;
  }
  .contact-list svg {
    width: 15px;
    height: 15px;
    margin-right: 16px;
    fill: var(--card-text-soft);
  }

  .seal {
    position: absolute;
    left: 480px;
    top: 22px;
    width: 498px;
    height: 498px;
    border-radius: 50%;
    background: var(--seal-bg);
  }
  .seal .seal-dot {
    position: absolute;
    left: 155px;
    top: 110px;
    width: 188px;
    height: 188px;
    border-radius: 50%;
    background: var(--seal-dot);
  }
  .seal .seal-name {
    position: absolute;
    left: 0;
    width: 100%;
    top: 332px;
    text-align: center;
    font-size: 35px;
    font-weight: 500;
    letter-spacing: 0.8px;
    color: var(--seal-text);
    text-transform: uppercase;
    line-height: 1;
  }
  .seal .seal-tag {
    position: absolute;
    left: 0;
    width: 100%;
    top: 374px;
    text-align: center;
    font-size: 13px;
    font-weight: 500;
    letter-spacing: 1.2px;
    color: var(--seal-text);
    text-transform: uppercase;
  }
</style>
</head>
<body>
  <div class="business-card">
    <div class="brand-line serif">
      <div class="brand-name">Tessa Brundle</div>
      <div class="brand-tag">Guidance and Partnering</div>
    </div>

    <div class="person">
      <div class="person-name serif">Tessa Brundle, J.D.</div>
      <div class="person-role sans">Collaborative Lawyer</div>
      <div class="person-role sans">Certified Divorce Coach</div>
    </div>

    <ul class="contact-list sans">
      <li>
        <svg viewBox="0 0 16 16" aria-hidden="true"><path d="M3.5 1.5l2.6 2.6-1.5 2a8.5 8.5 0 0 0 5.3 5.3l2-1.5 2.6 2.6-1.8 2C7.2 14.8 1.2 8.8 1.5 3.3z"/></svg>
        <span>515/555-0143</span>
      </li>
      <li>
        <svg viewBox="0 0 16 16" aria-hidden="true"><path d="M1 3.5h14v9H1z M1.6 4.2L8 9l6.4-4.8" fill="none" stroke="rgba(255,255,255,0.72)" stroke-width="1.6"/><rect x="1" y="3.5" width="14" height="9"/></svg>
        <span>tbjd@quellmail.net</span>
      </li>
      <li>
        <svg viewBox="0 0 16 16" aria-hidden="true"><circle cx="8" cy="8" r="6.5" fill="none" stroke="rgba(255,255,255,0.72)" stroke-width="1.8"/><path d="M4 5.5h3.5v3H5zM9 9.5h3l-1.5 3H9z"/></svg>
        <span>Guidanceandpartnering.com</span>
      </li>
    </ul>

    <div class="seal">
      <div class="seal-dot"></div>
      <div class="seal-name serif">Tessa Brundle</div>
      <div class="seal-tag serif">Guidance and Partnering</div>
    </div>
  </div>
</body>
</html>
```